Fatigued and Overloaded by COVID Messages? We need original illustrations to show that.

Everywhere you look there are messages about COVID. That is leading many people to feel fatigued and overloaded by the messages.

We surveyed U.S. adults March 20th - 24th, 2020 and measured message fatigue, information overload, perceived repetition, and perceived exaggeration. Here is how participants responded:

When it comes to coronavirus . . .
55% feel exhausted by all the messages.
54% feel overloaded by the amount of information.
51% feel that the messages are repetitive.
47% feel like messages exaggerate how bad it is.

In other words, almost half of U.S. adults show signs of message fatigue, information overload, perceived message repetition, and perceived message exaggeration.

We will continue to survey 400 adults every week for the next 16 weeks. Each time we will measure message fatigue, information overload, perceived repetition, and perceived exaggeration. We expect that it will increase over time.

What are we looking for? We need innovative and original illustrations that attempt to communicate these findings. The illustrations would visualize message fatigue, information overload, perceived message repetition, and perceived message exaggeration.

What sort of visual are we looking for? Our preference is for an original illustration (or set of illustrations). Our preference is for creative and powerful illustrations, but we are also open to the creative and well-executed infographics.

We need these images fast . We will award monetary prizes to the 3 best designs. If we like more than that, then we might purchase more (e.g., in past contests, we have purchased as many as 30 designs).

What we will need:
(1) The illustrations must be original and we will need the photoshop and/or illustrator files for all artwork. (By original, we mean that the illustrations are 100% created by you. Our organization requires that we utilize only original illustrated work. We have had issues with free imagery being pirated and reposted as free. We sidestep that issue by just having everything created.)

(2) The illustration should say, somewhere: "Based on a survey of 400 U.S. adults conducted March 20 - 24th, 2020."

(3) We will have almost 4 months worth of data by the time this is done. In other words, the illustrations might be able to help us present that weekly data.

(4) We have conducted other Artvendo projects. It might be helpful to examine designs we liked in the past. For example, here is another COVID project we just finished:

https://jobs.artvendo-example.com/job/5162048

Target Market(s)

U.S. adults

Requirements
Must have
• Original illustrations. Mobile friendly design. People will view this on their smartphones.
Nice to have
• A design that we can use to communicate the data across time.

```html
<!DOCTYPE html>
<html lang="en">
<head>
<meta charset="utf-8">
<title>Fatigued and Overloaded by COVID Messages?</title>
<link rel="stylesheet" href="https://fonts.googleapis.com/css2?family=Montserrat:wght@400;600;700;800&display=swap">
<style>
  :root {
    --teal: #239cc0;
    --salmon: #f6a195;
    --white: #ffffff;
    --art-light: #5fb7d2;
  }
  * { margin: 0; padding: 0; box-sizing: border-box; }
  html, body { width: 1200px; height: 3129px; overflow: hidden; background: var(--white); }
  body { position: relative; font-family: "Montserrat", sans-serif; color: var(--white); }

  .headline {
    position: absolute; top: 108px; left: 0; width: 1200px;
    text-align: center; color: var(--teal);
    font-weight: 800; font-size: 64px; line-height: 82px; letter-spacing: 1px;
  }

  .stat-panel {
    position: absolute; left: 0; width: 1200px; height: 550px;
    background: var(--teal);
    border-bottom-right-radius: 88px;
  }
  .stat-panel--fatigue { top: 384px; }
  .stat-panel--overload { top: 1006px; }
  .stat-panel--repetition { top: 1629px; }
  .stat-panel--exaggeration { top: 2251px; }

  .stat-art {
    position: absolute; left: 60px; top: 30px; width: 560px; height: 520px;
    background: linear-gradient(160deg, var(--art-light) 0%, var(--teal) 55%, rgba(246,161,149,0.55) 100%);
    border-radius: 24px 24px 0 0;
  }

  .stat-copy { position: absolute; left: 678px; width: 446px; top: 0; height: 100%; text-align: right; }
  .stat-figure {
    position: absolute; right: 0; top: 78px;
    font-weight: 700; font-size: 208px; line-height: 1; letter-spacing: -2px;
  }
  .stat-line { position: absolute; right: 0; white-space: nowrap; font-weight: 700; line-height: 1; }
  .stat-line--lead { font-size: 57px; letter-spacing: 1px; }
  .stat-line--tail { font-size: 38px; }
  .stat-line--small { font-size: 28px; }
  .stat-line--top { top: 284px; }
  .stat-line--bottom { top: 342px; }

  .stat-bar {
    position: absolute; left: 0; top: 406px; width: 446px; height: 33px;
    background: var(--white);
  }
  .stat-bar-fill { height: 100%; background: var(--salmon); }

  .source-note {
    position: absolute; top: 2930px; left: 0; width: 1200px;
    text-align: center; color: var(--teal);
    font-weight: 400; font-size: 30px; line-height: 38px;
  }
</style>
</head>
<body>
  <h1 class="headline">Fatigued and Overloaded<br>by COVID Messages?</h1>

  <section class="stat-panel stat-panel--fatigue">
    <div class="stat-art" role="img" aria-label="Illustration of an exhausted man slumped in an office chair beside a glowing laptop"></div>
    <div class="stat-copy">
      <div class="stat-figure">55%</div>
      <div class="stat-line stat-line--lead stat-line--top">feel exhausted</div>
      <div class="stat-line stat-line--tail stat-line--bottom">by all the messages.</div>
      <div class="stat-bar"><div class="stat-bar-fill" style="width:55%"></div></div>
    </div>
  </section>

  <section class="stat-panel stat-panel--overload">
    <div class="stat-art" role="img" aria-label="Illustration of a person buried under charts, envelopes and information icons"></div>
    <div class="stat-copy">
      <div class="stat-figure">54%</div>
      <div class="stat-line stat-line--lead stat-line--top">feel overloaded</div>
      <div class="stat-line stat-line--small stat-line--bottom">by the amount of information.</div>
      <div class="stat-bar"><div class="stat-bar-fill" style="width:54%"></div></div>
    </div>
  </section>

  <section class="stat-panel stat-panel--repetition">
    <div class="stat-art" role="img" aria-label="Illustration of a woman looking at her phone surrounded by circular arrows around an envelope and info icon"></div>
    <div class="stat-copy">
      <div class="stat-figure">51%</div>
      <div class="stat-line stat-line--tail" style="top:284px">feel that the messages</div>
      <div class="stat-line stat-line--lead" style="top:328px">are repetitive.</div>
      <div class="stat-bar"><div class="stat-bar-fill" style="width:51%"></div></div>
    </div>
  </section>

  <section class="stat-panel stat-panel--exaggeration">
    <div class="stat-art" role="img" aria-label="Illustration of a man carrying a giant virus particle with a speech bubble showing a tiny virus"></div>
    <div class="stat-copy">
      <div class="stat-figure">47%</div>
      <div class="stat-line stat-line--tail" style="top:290px;font-size:44px">feel like messages</div>
      <div class="stat-line stat-line--small" style="top:344px;font-size:31px">exaggerate how bad it is.</div>
      <div class="stat-bar"><div class="stat-bar-fill" style="width:47%"></div></div>
    </div>
  </section>

  <p class="source-note">Based on a survey of 400 U.S. adults<br>conducted March 20 - 24th, 2020.</p>
</body>
</html>
```